'Wedding Business" Business Card Design

dj services for weddings and parties, uplighting, event planning, day of coordination for weddings, photography for weddings and other events.

Would like raised print and metallic also if possible. Elegant design, yet modern. This is a wedding business and should describe our goals and main services - DJ/lighting, wedding and event planning, photography. slogan "Simply Incredible, Incredibly simple" or "Your Dreams. Our Experience. The Perfect Match" Our goal is to provide multiple services to make it easier for the bride and groom almost like a one stop shop. Feel free to use the slogan or leave it out , we just want to really stand out against the competition. You can also get more info on our website www.brightlanestudios.com - we are working to get the brightlanenc.com site pointed to our current site!

there should be 2 files attached, if they did not go through please email events@brightlanenc.com or brightlanestudios@mailbox.test
Updates

Thank you all for your help, we have decided what we like but would like to make some changes, we need to order these asap so please let us know if you can help.

Reason: Wasn't able to pick it out in time! So Sorry but we know what we want!!

Industry/Entity Type

Business

Contact Information for Business Card

Marcus and Leona Whitcombe
555-318-2047
555-720-4861
Bright Lane Studios, Events, & Photography
EMAIL:Events@BrightLaneNC.com
www.brightlanenc.com

```html
<!DOCTYPE html>
<html lang="en">
<head>
<meta charset="utf-8">
<title>Bright Lane Studios – Business Card</title>
<link rel="stylesheet" href="https://fonts.googleapis.com/css2?family=Raleway:wght@400;500&family=Cormorant+Garamond:ital,wght@1,500&display=swap">
<style>
  :root {
    --backdrop: #6b5238;
    --card: #000000;
    --frame: #d9d9d9;
    --text-bright: #f0f0f0;
    --text-soft: #c4c4c4;
    --text-muted: #9a9a9a;
    --silver-light: #e6e6e6;
    --silver-dark: #7d7d7d;
  }
  * { margin: 0; padding: 0; box-sizing: border-box; }
  html, body {
    width: 1200px; height: 900px; overflow: hidden;
    background: var(--backdrop);
  }
  .canvas { position: relative; width: 1200px; height: 900px; }

  .card {
    position: absolute; top: 32px;
    width: 490px; height: 834px;
    background: var(--card);
  }
  .card--front { left: 86px; }
  .card--back  { left: 618px; }
  .card__frame {
    position: absolute; inset: 10px;
    border: 1px solid var(--frame);
  }

  .ornament {
    position: absolute; left: 44px; width: 402px;
    background: linear-gradient(90deg, var(--silver-dark), var(--silver-light) 50%, var(--silver-dark));
    opacity: 0.55; border-radius: 40px;
  }
  .ornament--top { top: 30px; height: 130px; }
  .ornament--bottom { top: 680px; height: 128px; }

  .line {
    position: absolute; left: 0; width: 490px; text-align: center;
    font-family: "Raleway", sans-serif; color: var(--text-bright); white-space: nowrap;
  }
  .company { top: 172px; font-size: 28px; letter-spacing: 0.5px; }
  .company-sub { top: 207px; font-size: 24px; color: var(--text-soft); }
  .owners { top: 245px; font-size: 19px; }
  .phone-1 { top: 273px; font-size: 19px; }
  .phone-2 { top: 300px; font-size: 19px; }
  .email { top: 335px; font-size: 18px; color: var(--text-soft); }
  .web { top: 362px; font-size: 18px; color: var(--text-soft); }
  .social { top: 389px; font-size: 18px; color: var(--text-soft); }

  .divider { position: absolute; top: 424px; left: 38px; }

  .services {
    position: absolute; top: 446px; left: 0; width: 490px;
    list-style: none; text-align: center;
    font-family: "Raleway", sans-serif; font-size: 20px; line-height: 29px;
    color: var(--text-soft);
  }
  .services__note { font-size: 16px; line-height: 22px; color: var(--text-muted); }

  .brand-name {
    position: absolute; top: 300px; left: 0; width: 490px; text-align: center;
    font-family: "Raleway", sans-serif; font-weight: 500; font-size: 92px; line-height: 110px;
    color: var(--silver-light);
  }
  .slogan {
    position: absolute; top: 770px; left: 0; width: 490px; text-align: center;
    font-family: "Cormorant Garamond", serif; font-style: italic; font-weight: 500;
    font-size: 32px; color: var(--text-bright); white-space: nowrap;
  }
  .slogan__soft { color: var(--text-muted); }
</style>
</head>
<body>
<main class="canvas">
  <section class="card card--front">
    <div class="card__frame"></div>
    <div class="ornament ornament--top" role="img" aria-label="Silver scrollwork flourish"></div>

    <p class="line company">BRIGHT LANE STUDIOS</p>
    <p class="line company-sub">EVENTS, &amp; PHOTOGRAPHY</p>
    <p class="line owners">Marcus and Leona Whitcombe</p>
    <p class="line phone-1">555-318-2047</p>
    <p class="line phone-2">555-720-4861</p>
    <p class="line email">Email:Events@BrightLaneNC.com</p>
    <p class="line web">www.brightlanenc.com</p>
    <p class="line social">Fb:BrightLaneStudiosEventsPhotography</p>

    <svg class="divider" width="414" height="10" viewBox="0 0 414 10">
      <line x1="0" y1="5" x2="154" y2="5" stroke="#bdbdbd" stroke-width="1.2"/>
      <path d="M166 5 Q190 -1 207 5 Q224 11 248 5" fill="none" stroke="#bdbdbd" stroke-width="1.4"/>
      <line x1="260" y1="5" x2="414" y2="5" stroke="#bdbdbd" stroke-width="1.2"/>
    </svg>

    <ul class="services">
      <li>DJ Services</li>
      <li>Lighting Design</li>
      <li>Event &amp; Wedding Planning</li>
      <li>Lifestyle Photography</li>
      <li>Wedding Websites</li>
      <li>Online Planning Tools</li>
      <li>Coustomized Design</li>
      <li class="services__note">Invitations, Programs, Stationary, Etc</li>
    </ul>

    <div class="ornament ornament--bottom" role="img" aria-label="Silver scrollwork flourish"></div>
  </section>

  <section class="card card--back">
    <div class="card__frame"></div>
    <p class="brand-name">Bright<br>Lane</p>
    <p class="slogan">Truly <span class="slogan__soft">Effortless.</span> Effortlessly <span class="slogan__soft">True</span></p>
  </section>
</main>
</body>
</html>
```